creation of business cards for Velanto Sàrl

Velanto S% 26 # 224; rl is a soci% 26 # 233; t% 26 # 233; consultancy that accompanies companies in the development of their business on the market% 26 # 233; Switzerland by providing strategic contacts or market information; and by providing administrative or logistical support. Our consulting skills focus on sectors% 26 # 224; high value added% 26 # 233; e, such as trade in food goods% 26 # 39amp; drinks, fashion% 26amp; lifestyle, products and services for% 26 # 233; s in high-tech industries (pharmaceutical, chemical, m% 26 # 233; pricy 26% 23 #; cision) or sustainable solutions (% 26 # 233; energies renewable, mat% 26 # 233; recyclable materials). As part of the launch of our activity% 26 # 233;, we need% 26 # 39;% 26 # 233; to establish business cards to d% 26 # 233; work our new customers (Swiss or international).

Target Market(s)

Companies wishing to develop their activity% 26 # 233; s in Switzerland or% 26 # 224; l% 26 # 39;% 26 # 233; abroad (mainly in Europe).

Contact Information for Business Card

Prénom NOM
Velanto Sàrl
Bureau de Marvoisin
Rue des Tilleuls 47, 2000 Neuchâtel
Tél. : 032 718 46 39
info@velanto-example.ch
www.velanto-example.ch

Font styles to use
Serif
Sans Serif

Colors

Designer to choose colors to be used in the design.

Requirements
Must have
• The logo The name of the company% 26 # 233; t% 26 # 233; (Velanto S% 26 # 224; rl) One field for the mailing address One field for the number% 26 # 233; ro de t% 26 # 233; l% 26 # 233; phone One field for the % 26 # 39; email address and website

```html
<!DOCTYPE html>
<html lang="fr">
<head>
<meta charset="utf-8">
<title>Velanto Sàrl – cartes de visite</title>
<link rel="stylesheet" href="https://fonts.googleapis.com/css2?family=Michroma&family=Poppins:wght@300;400&display=swap">
<style>
  :root {
    --backdrop: #e8e5e0;
    --navy: #1e3d52;
    --brand-teal: #1f4c62;
    --paper: #ffffff;
    --soft-line: rgba(255,255,255,0.55);
    --icon: #c9d3da;
  }
  * { margin: 0; padding: 0; box-sizing: border-box; }
  html, body { width: 900px; height: 1200px; overflow: hidden; }
  body { background: var(--backdrop); position: relative; font-family: "Poppins", sans-serif; }

  .card {
    position: absolute; left: 80px; width: 734px; height: 430px;
    border-radius: 22px; overflow: hidden; background: var(--navy);
    box-shadow: 0 4px 12px rgba(0,0,0,0.18);
  }
  .card--front { top: 127px; }
  .card--back { top: 645px; }

  .front-header {
    position: absolute; left: 0; top: 0; width: 100%; height: 200px;
    background: var(--paper);
  }
  .brand { position: absolute; left: 163px; top: 73px; display: flex; align-items: center; }
  .brand-square { width: 62px; height: 62px; background: var(--brand-teal); border-radius: 10px; }
  .brand-name {
    margin-left: 36px; font-family: "Michroma", sans-serif; font-size: 43px;
    color: var(--brand-teal); letter-spacing: 1px; line-height: 1;
  }

  .holder { position: absolute; right: 384px; top: 291px; text-align: right; color: var(--paper); }
  .holder-name { font-family: "Michroma", sans-serif; font-size: 19px; letter-spacing: 1px; line-height: 1.2; }
  .holder-company { font-family: "Michroma", sans-serif; font-size: 13px; letter-spacing: 1.6px; margin-top: 6px; color: #dfe6eb; }

  .divider { position: absolute; left: 367px; top: 250px; width: 1px; height: 124px; background: var(--soft-line); }

  .contact { position: absolute; left: 385px; top: 243px; color: var(--paper); font-size: 15.5px; line-height: 25px; }
  .contact-office { margin-bottom: 8px; }
  .contact-line { display: flex; align-items: center; height: 26px; }
  .contact-line svg { width: 17px; height: 17px; margin-right: 12px; flex: none; }

  .back-mark {
    position: absolute; left: 0; top: 192px; width: 100%;
    display: flex; justify-content: center; align-items: center;
  }
  .back-square { width: 40px; height: 40px; border: 2px solid var(--paper); margin-right: 22px; }
  .back-name { font-family: "Michroma", sans-serif; font-size: 34px; color: var(--paper); letter-spacing: 2px; line-height: 1; }
  .back-url {
    position: absolute; left: 0; bottom: 35px; width: 100%; text-align: center;
    font-family: "Michroma", sans-serif; font-size: 15px; letter-spacing: 3.5px; color: var(--paper);
  }
</style>
</head>
<body>

<section class="card card--front">
  <header class="front-header">
    <div class="brand">
      <div class="brand-square"></div>
      <div class="brand-name">VELANTO</div>
    </div>
  </header>

  <div class="holder">
    <div class="holder-name">PRÉNOM NOM</div>
    <div class="holder-company">VELANTO SÀRL</div>
  </div>

  <div class="divider"></div>

  <div class="contact">
    <div class="contact-office">Bureau de Marvoisin<br>Rue des Tilleuls 47, 2000 Neuchâtel</div>
    <div class="contact-line">
      <svg viewBox="0 0 24 24" aria-hidden="true"><path fill="var(--icon)" d="M6.6 10.8a15.2 15.2 0 0 0 6.6 6.6l2.2-2.2c.3-.3.7-.4 1-.2 1.1.4 2.3.6 3.6.6.6 0 1 .4 1 1V20c0 .6-.4 1-1 1A17 17 0 0 1 3 4c0-.6.4-1 1-1h3.5c.6 0 1 .4 1 1 0 1.3.2 2.5.6 3.6.1.3 0 .7-.2 1z"/></svg>
      032 718 46 39
    </div>
    <div class="contact-line">
      <svg viewBox="0 0 24 24" aria-hidden="true"><rect x="2" y="5" width="20" height="14" fill="var(--icon)"/><path d="M2 5l10 8 10-8" fill="none" stroke="var(--navy)" stroke-width="1.6"/></svg>
      info@velanto-example.ch
    </div>
    <div class="contact-line">
      <svg viewBox="0 0 24 24" aria-hidden="true" fill="none" stroke="var(--icon)" stroke-width="1.6"><circle cx="12" cy="12" r="9.5"/><ellipse cx="12" cy="12" rx="4" ry="9.5"/><path d="M2.5 12h19M4 7h16M4 17h16"/></svg>
      www.velanto-example.ch
    </div>
  </div>
</section>

<section class="card card--back">
  <div class="back-mark">
    <div class="back-square"></div>
    <div class="back-name">VELANTO</div>
  </div>
  <div class="back-url">WWW.VELANTO-EXAMPLE.CH</div>
</section>

</body>
</html>
```